Kestrel Builders Business Card Design Project

Clean sharp business card
Ability to write on back of card
Details for the card -
Address: PO Box 5867, Tingapla, Qld, 4173
ABN: 47 305 961 220
BSA LIC 2650874
Ph: 07 3562 4470
Fax: 07 3562 4475
Email: kestrelbuilders@mailbrook.com.au

```html
<!DOCTYPE html>
<html lang="en">
<head>
<meta charset="utf-8">
<title>Kestrel Builders – Business Card</title>
<link rel="stylesheet" href="https://fonts.googleapis.com/css2?family=Tinos:wght@400&display=swap">
<style>
  :root {
    --backdrop: #45232a;
    --card: #ffffff;
    --orange: #f07a36;
    --amber: #fbb034;
    --charcoal: #363636;
    --steel: #8c8c8c;
    --ink: #2b2b2b;
    --on-orange: #ffffff;
  }
  html, body {
    margin: 0;
    padding: 0;
    width: 1200px;
    height: 1104px;
    overflow: hidden;
    background: var(--backdrop);
  }
  .card {
    position: absolute;
    left: 330px;
    top: 72px;
    width: 540px;
    height: 960px;
    background: var(--card);
    font-family: "Tinos", "Times New Roman", serif;
    overflow: hidden;
  }
  .brand {
    position: absolute;
    left: 70px;
    top: 160px;
    display: flex;
    align-items: center;
    gap: 14px;
  }
  .brand-dot {
    width: 22px;
    height: 22px;
    border-radius: 50%;
    background: var(--orange);
  }
  .brand-name {
    font-size: 42px;
    color: var(--steel);
    letter-spacing: 1px;
  }
  .blocks {
    position: absolute;
    left: 0;
    top: 0;
    width: 540px;
    height: 960px;
  }
  .postal {
    position: absolute;
    right: 30px;
    top: 632px;
    text-align: right;
    color: var(--on-orange);
    font-size: 22px;
    line-height: 30px;
  }
  .contact {
    position: absolute;
    left: 22px;
    bottom: 26px;
    color: var(--ink);
    font-size: 18px;
    line-height: 25px;
  }
</style>
</head>
<body>
  <div class="card">
    <div class="brand">
      <span class="brand-dot"></span>
      <span class="brand-name">Kestrel Builders</span>
    </div>

    <svg class="blocks" viewBox="0 0 540 960" aria-hidden="true">
      <polygon points="212,610 236,610 214,780 190,780" fill="var(--charcoal)"/>
      <polygon points="236,610 540,610 540,780 214,780" fill="var(--orange)"/>
      <rect x="0" y="818" width="394" height="142" fill="var(--amber)"/>
      <rect x="408" y="800" width="132" height="160" fill="var(--charcoal)"/>
    </svg>

    <div class="postal">
      PO Box 5867<br>
      Wrenhaven, Qld, 4188<br>
      ABN: 47 305 961 220<br>
      BSA LIC 2650874
    </div>

    <div class="contact">
      Ph: 07 3562 4470<br>
      Fax: 07 3562 4475<br>
      Email: kestrelbuilders@mailbrook.com.au
    </div>
  </div>
</body>
</html>
```